VelloTask Business Card

Our company is called VelloTask and we are based in Tel Aviv, Israel. We create innovative and exciting methods for getting people on the web engaged with content. We need a cool yet professional business card that will represent our management level employees. keep in mind this is a start up company with a young atmosphere. You can be inspired by our logo (file attached, make sure you have the right font "Ubuntu-Condensed") Use the colors that are used in the logo and create a colourful and professional business card.

```html
<!DOCTYPE html>
<html lang="en">
<head>
<meta charset="utf-8">
<title>VelloTask Business Cards</title>
<link rel="stylesheet" href="https://fonts.googleapis.com/css2?family=Ubuntu+Condensed&family=Ubuntu:wght@400;500&display=swap">
<style>
  :root {
    --stage: #262626;
    --card-dark: #3b3b3d;
    --card-light: #fdfcf9;
    --ink: #1f1f1f;
    --accent-blue: #1f8ed0;
    --pink: #e8287a;
    --purple: #8e3a96;
    --sky: #4db3e0;
  }
  * { margin: 0; padding: 0; box-sizing: border-box; }
  html, body { width: 1200px; height: 800px; overflow: hidden; }
  body {
    background: var(--stage);
    font-family: "Ubuntu", sans-serif;
    color: var(--ink);
    position: relative;
  }
  .card {
    position: absolute;
    overflow: hidden;
    box-shadow: 0 2px 6px rgba(0,0,0,.45);
  }
  .card--landscape { width: 413px; height: 235px; }
  .card--portrait { width: 235px; height: 413px; }
  .card--back { background: var(--card-dark); }
  .card--front { background: var(--card-light); }

  .pattern-area {
    position: absolute; inset: 0;
    background: linear-gradient(120deg, #4a3444 0%, #3b3b3d 50%, #34404a 100%);
  }

  .wordmark {
    position: absolute;
    font-family: "Ubuntu Condensed", "Ubuntu", sans-serif;
    font-weight: 400;
    line-height: 1;
    white-space: nowrap;
  }
  .wordmark--light { color: #ffffff; font-size: 50px; }
  .wordmark--dark { color: var(--ink); }

  .brand-dot {
    position: absolute;
    border-radius: 50%;
    background: var(--pink);
  }

  .name { position: absolute; font-size: 26px; font-weight: 400; white-space: nowrap; }
  .role { position: absolute; font-size: 12px; color: var(--accent-blue); white-space: nowrap; }
  .details { position: absolute; font-size: 12px; line-height: 18px; white-space: nowrap; }
  .details--centered, .name--centered, .role--centered { text-align: center; left: 0; right: 0; }
  .contact-rule {
    position: absolute;
    width: 2px;
    background: var(--accent-blue);
  }
</style>
</head>
<body>

  <section class="card card--landscape card--back" style="left:53px; top:158px;">
    <div class="pattern-area" role="img" aria-label="Decorative pattern of scattered colourful circles on charcoal"></div>
    <span class="wordmark wordmark--light" style="left:136px; top:178px;">vellotask</span>
  </section>

  <section class="card card--landscape card--back" style="left:482px; top:158px;">
    <div class="pattern-area" role="img" aria-label="Decorative pattern of scattered colourful circles on charcoal"></div>
    <span class="wordmark wordmark--light" style="left:34px; top:100px;">vellotask</span>
  </section>

  <section class="card card--landscape card--front" style="left:53px; top:408px;">
    <div class="brand-dot" style="left:80px; top:60px; width:60px; height:60px;"></div>
    <span class="wordmark wordmark--dark" style="left:30px; top:155px; font-size:36px;">vellotask</span>
    <h1 class="name" style="left:249px; top:38px;">Noa Levran</h1>
    <p class="role" style="left:252px; top:68px;">Co-Founder &amp; CEO</p>
    <p class="details" style="left:249px; top:98px;">58 Meridian Street,<br>Tel Aviv, Israel 61000</p>
    <div class="contact-rule" style="left:250px; top:153px; height:46px;"></div>
    <p class="details" style="left:258px; top:148px;">+972-541236780<br>noa@vellotask.com<br>www.vellotask.com</p>
  </section>

  <section class="card card--landscape card--front" style="left:482px; top:408px;">
    <div class="brand-dot" style="left:189px; top:20px; width:36px; height:36px;"></div>
    <span class="wordmark wordmark--dark" style="left:0; right:0; text-align:center; top:78px; font-size:26px;">vellotask</span>
    <h1 class="name name--centered" style="top:122px; font-size:24px;">Noa Levran</h1>
    <p class="role role--centered" style="top:150px;">Co-Founder &amp; CEO</p>
    <p class="details details--centered" style="top:167px;">58 Meridian Street, Tel Aviv, Israel 61000</p>
    <p class="details details--centered" style="top:192px; line-height:16px;">+972-541236780 // noa@vellotask.com<br>www.vellotask.com</p>
  </section>

  <section class="card card--portrait card--front" style="left:912px; top:230px;">
    <div class="brand-dot" style="left:85px; top:52px; width:64px; height:64px;"></div>
    <span class="wordmark wordmark--dark" style="left:0; right:0; text-align:center; top:140px; font-size:34px;">vellotask</span>
    <h1 class="name name--centered" style="top:214px;">Noa Levran</h1>
    <p class="role role--centered" style="top:245px;">Co-Founder &amp; CEO</p>
    <p class="details details--centered" style="top:276px;">58 Meridian Street,<br>Tel Aviv, Israel 61000</p>
    <p class="details details--centered" style="top:326px; line-height:17px;">+972-541236780<br>noa@vellotask.com</p>
    <p class="details details--centered" style="top:360px; font-size:14px;">www.vellotask.com</p>
  </section>

</body>
</html>
```